We need business cards for our Kashmiri Indian Takeaway Shop. our business sells authentic Kashmiri Cuisine. We also offer catering services and have a BYO Function Room available for private bookings. We would like to see simple but stylish designs that feature Moroccan or Arabic style patterns/ borders and use golds, deep reds, pearl/cream and a touch of black or white. We do not want pictures of curries or Indian spices, chillies etc. The final design should communicate sumptuous, exotic dining.

Target Market(s)

Indian food lovers

Industry/Entity Type

Catering

Contact Information for Business Card

Rafi's Kitchen Authentic Kashmiri Indian Cuisine

Colors
ec2027
fce8d3
fcca95
faa54b

Requirements
Must have
• Simple but stylish design, using Moroccan/Arabic inspired borders or features
Should not have
• Pictures of curries, spices, food etc

```html
<!DOCTYPE html>
<html lang="en">
<head>
<meta charset="utf-8">
<title>Rafi's Kitchen – Business Card</title>
<link href="https://fonts.googleapis.com/css2?family=Gelasio&family=Kalam:wght@400&display=swap" rel="stylesheet">
<style>
  :root {
    --backdrop: #cdd4ce;
    --card-red: #7a0a0a;
    --card-wine: #3a0a10;
    --card-dark: #150608;
    --accent-orange: #faa54b;
    --accent-gold: #fcca95;
    --pearl: #f3e6e6;
    --streak: rgba(255, 200, 210, 0.9);
  }
  * { margin: 0; padding: 0; box-sizing: border-box; }
  html, body {
    width: 1200px;
    height: 1000px;
    overflow: hidden;
    background: var(--backdrop);
  }
  .canvas {
    width: 1200px;
    height: 1000px;
    display: flex;
    align-items: center;
    justify-content: center;
  }
  .business-card {
    position: relative;
    width: 1000px;
    height: 572px;
    overflow: hidden;
    background:
      radial-gradient(ellipse 70% 60% at 85% 0%, var(--card-red) 0%, rgba(122,10,10,0) 75%),
      linear-gradient(160deg, #6a0a0c 0%, var(--card-wine) 45%, var(--card-dark) 100%);
    box-shadow: 0 18px 40px rgba(0,0,0,0.35);
  }
  .card-art {
    position: absolute;
    left: 0;
    top: 0;
    width: 1000px;
    height: 572px;
  }
  .card-content {
    position: absolute;
    left: 300px;
    top: 70px;
    width: 560px;
    text-align: center;
    font-family: "Gelasio", "Palatino Linotype", serif;
  }
  .brand-name {
    color: var(--accent-orange);
    font-size: 46px;
    font-weight: 400;
    line-height: 51px;
    letter-spacing: 1px;
  }
  .brand-tagline {
    color: var(--pearl);
    font-size: 20px;
    line-height: 26px;
    margin-top: 4px;
  }
  .person-name {
    font-family: "Kalam", cursive;
    color: var(--accent-orange);
    font-size: 64px;
    line-height: 64px;
    margin-top: 20px;
  }
  .person-role {
    color: var(--pearl);
    font-size: 32px;
    line-height: 38px;
    margin-top: 34px;
  }
  .contact-list {
    list-style: none;
    color: var(--pearl);
    font-size: 24px;
    line-height: 32px;
    margin-top: 20px;
  }
</style>
</head>
<body>
  <main class="canvas">
    <article class="business-card">
      <svg class="card-art" viewBox="0 0 1000 572" aria-hidden="true">
        <defs>
          <radialGradient id="streakGlow" cx="0.5" cy="0.5" r="0.5">
            <stop offset="0" stop-color="#ffd8e0" stop-opacity="0.9"/>
            <stop offset="0.35" stop-color="#c0485a" stop-opacity="0.5"/>
            <stop offset="1" stop-color="#7a0a14" stop-opacity="0"/>
          </radialGradient>
        </defs>
        <g class="light-streak">
          <ellipse cx="580" cy="251" rx="400" ry="12" fill="url(#streakGlow)"/>
          <ellipse cx="580" cy="251" rx="360" ry="2" fill="var(--streak)"/>
        </g>
        <g class="arabesque-border" fill="none" stroke="var(--accent-gold)" stroke-opacity="0.75">
          <rect x="22" y="22" width="956" height="528" stroke-width="2"/>
          <rect x="32" y="32" width="936" height="508" stroke-width="1"/>
          <g stroke-width="1.5">
            <path d="M22 52 L52 22 M32 62 L62 32"/>
            <path d="M978 52 L948 22 M968 62 L938 32"/>
            <path d="M22 520 L52 550 M32 510 L62 540"/>
            <path d="M978 520 L948 550 M968 510 L938 540"/>
          </g>
          <g fill="var(--accent-gold)" fill-opacity="0.75" stroke="none">
            <path d="M500 15 L508 27 L500 39 L492 27 Z"/>
            <path d="M500 533 L508 545 L500 557 L492 545 Z"/>
            <path d="M15 286 L27 278 L39 286 L27 294 Z"/>
            <path d="M985 286 L973 278 L961 286 L973 294 Z"/>
          </g>
        </g>
      </svg>
      <div class="card-content">
        <h1 class="brand-name">Rafi's Kitchen</h1>
        <p class="brand-tagline">Authentic Kashmiri Indian Cuisine</p>
        <p class="person-name">Tariq Rafi</p>
        <p class="person-role">Owner &amp; Chef</p>
        <ul class="contact-list">
          <li>Takeaway Shop &amp; Catering</li>
          <li>BYO Function Room - bookings essential</li>
          <li>14 Ridge Lane, Marlow Qld</li>
          <li>07- 5550 1842</li>
        </ul>
      </div>
    </article>
  </main>
</body>
</html>
```